Create a banner for me that embodies my health and well being package.

I am an intuitive counselor with a busy practice helping clients to shift their blocks and move forward in their lives.
I have created a package called '9 paths home again'
I am wanting a banner to put on my website page, facebook page and to use as a letter head in mailouts.
My ideal clients are those who want to create change in their lives and who invest money in themselves and their personal and spiritual growth.
I am different to regular life coaches as my sessions have a spiritual twist to them creating much deeper change in my clients.
I would like the banner to be mainly font with the title of the progam: 9 Paths Home Again (no other wording) (something along the lines of the Blackjack font) and that ties in with the theme of my website. I'm not sure what else I want with it and am looking for ideas.
Website:
www.brightwillowhealing.com.au
I also have a current facebook page for the business:
https://www.facebook.com/Brightwillow-Healing-Studio-502718364091547/
(Note: I am about to drop my logo and business name and move to using my own name - the rest of the website will remain the same).
I have attached a doc with the draft of what wording will be on the website page any advertising will link to, to give you an idea of what the program is about.

Target Market(s)

People who invest money on themselves who are looking to improve their emotional well being and creating change in their life. Majority are middle aged women (also younger females and some men)

Industry/Entity Type

Health And Wellness

Font styles to use
Other font styles liked:
• I like Blackjack and Amienne. Along those lines.

Requirements
Must have
• Attractive, modern and GREAT font.
Nice to have
• Surprise me with something amazing!
• I love the colours in the 2 images I have up loaded as they represent the heart chakra colours. They could be a feature on the banner or blurred into the background.
Should not have
• Even though my work is quite spiritual I don't want it to look woo woo (meaning airy fairy spiritual stuff!)

```html
<!DOCTYPE html>
<html lang="en">
<head>
<meta charset="utf-8">
<title>9 Paths Home Again – Banner</title>
<link rel="stylesheet" href="https://fonts.googleapis.com/css2?family=Bodoni+Moda:wght@400;500&family=Roboto:ital,wght@0,400;1,900&display=swap">
<style>
  :root{
    --frame-blue:#2f7fc6;
    --frame-blue-dark:#1d5fa3;
    --frame-blue-light:#6fb2e6;
    --panel:#ffffff;
    --pebble-light:#eef2ee;
    --pebble-mid:#d5ddd8;
    --navy:#3c4a6e;
    --slate:#6f7d9c;
    --leaf:#7aa33a;
    --sage:#a7c08a;
    --lotus-bg:#8fc23f;
    --lotus-bg-deep:#5e9a22;
    --lotus-pink:#e2568f;
    --badge-red:#ec2453;
    --ink:#111111;
  }
  html,body{margin:0;padding:0;overflow:hidden;background:#ffffff;}
  .banner{
    position:relative;width:1200px;height:583px;overflow:hidden;
    background:linear-gradient(135deg,var(--frame-blue-light) 0%,var(--frame-blue) 40%,var(--frame-blue-dark) 100%);
  }
  .banner__art{position:absolute;inset:0;display:block;}
  .title-number{font-family:"Roboto",sans-serif;font-weight:900;font-style:italic;fill:#fff;}
  .title-main{font-family:"Roboto",sans-serif;font-weight:400;fill:var(--ink);letter-spacing:-3px;}
  .title-sub{font-family:"Bodoni Moda",serif;font-weight:400;fill:var(--ink);}
</style>
</head>
<body>
<div class="banner">
  <svg class="banner__art" viewBox="0 0 1200 583" width="1200" height="583" xmlns="http://www.w3.org/2000/svg">
    <defs>
      <linearGradient id="pebbleFade" x1="0" y1="0" x2="1" y2="0">
        <stop offset="0" stop-color="var(--pebble-mid)"/>
        <stop offset="0.55" stop-color="var(--pebble-light)"/>
        <stop offset="1" stop-color="#ffffff"/>
      </linearGradient>
      <radialGradient id="lotusGlow" cx="0.55" cy="0.5" r="0.6">
        <stop offset="0" stop-color="var(--lotus-pink)"/>
        <stop offset="0.35" stop-color="#c9508a"/>
        <stop offset="0.5" stop-color="var(--lotus-bg)"/>
        <stop offset="1" stop-color="var(--lotus-bg-deep)"/>
      </radialGradient>
      <clipPath id="panelClip"><rect x="26" y="24" width="1148" height="530"/></clipPath>
    </defs>

    <rect class="panel" x="26" y="24" width="1148" height="530" fill="var(--panel)"/>

    <g clip-path="url(#panelClip)">
      <rect x="26" y="24" width="720" height="530" fill="url(#pebbleFade)" role="img" aria-label="Soft photograph of smooth white pebbles"/>

      <path class="band-navy" d="M26 24 H560 C520 70 440 85 360 70 C250 50 150 40 26 60 Z" fill="var(--navy)"/>
      <path class="band-green" d="M470 24 H900 C870 60 780 75 680 70 C600 66 540 60 470 24 Z" fill="var(--leaf)"/>
      <path class="band-sage" d="M300 24 H520 C480 46 400 52 300 24 Z" fill="var(--sage)" opacity="0.8"/>

      <circle cx="1010" cy="294" r="300" fill="none" stroke="var(--slate)" stroke-width="8"/>
      <circle cx="760" cy="150" r="70" fill="#ffffff" stroke="var(--navy)" stroke-width="10"/>
      <circle cx="740" cy="294" r="80" fill="#ffffff" stroke="var(--navy)" stroke-width="10"/>
      <circle cx="760" cy="445" r="70" fill="#ffffff" stroke="var(--navy)" stroke-width="10"/>
      <circle cx="1010" cy="294" r="268" fill="#ffffff"/>
      <circle cx="1010" cy="294" r="258" fill="var(--navy)"/>
      <circle cx="1010" cy="294" r="246" fill="#ffffff"/>

      <circle cx="1010" cy="294" r="236" fill="url(#lotusGlow)" role="img" aria-label="Photograph of a pink lotus bud on a green background"/>
    </g>

    <circle class="title-badge" cx="221" cy="213" r="82" fill="var(--badge-red)"/>
    <text class="title-number" x="216" y="267" text-anchor="middle" font-size="152">9</text>

    <text class="title-main" x="88" y="390" font-size="132">paths</text>
    <line x1="405" y1="374" x2="650" y2="374" stroke="var(--ink)" stroke-width="3"/>
    <line x1="405" y1="386" x2="650" y2="386" stroke="var(--ink)" stroke-width="3"/>
    <text class="title-sub" x="90" y="472" font-size="74">home again</text>
  </svg>
</div>
</body>
</html>
```